Request for Business Card Design

Hi. My name is Marlena, I am looking for a new business card design for my company, Quillbrook Sensing Systems, LLC. I really like the design you did for Tavel Harvest and was hoping you could do something similar using our full logo and our mark. I am also open to any raised texture design using our mark. I have attached our full logo, which would need to be somewhere on the card, as well as the mark in both outline and full form, as well as our brand colors / guide. The card does not have to be white, as long as our logo and mark appear. I actually like darker colored business cards more, but am open to all options. If you are interested in working with me, please let me know. We would also take the business card design into letterhead design if you can do that.

```html
<!DOCTYPE html>
<html lang="en">
<head>
<meta charset="UTF-8">
<title>Quillbrook Sensing Systems — Business Card</title>
<link href="https://fonts.googleapis.com/css2?family=Barlow:wght@600&family=Montserrat:wght@400;500&display=swap" rel="stylesheet">
<style>
  :root {
    --backdrop: #3a3a3c;
    --card-white: #ffffff;
    --card-black: #1d1d1e;
    --brand-blue: #1a9fc9;
    --ink-dark: #3b3b3d;
    --ink-light: #ffffff;
    --rule-grey: #8a8a8a;
  }
  * { box-sizing: border-box; margin: 0; padding: 0; }
  html, body {
    width: 1200px; height: 1200px; overflow: hidden;
    background: var(--backdrop);
  }
  .canvas {
    width: 1200px; height: 1200px;
    display: flex; flex-direction: column; align-items: center; justify-content: center;
    gap: 60px;
  }
  .card {
    position: relative;
    width: 880px; height: 503px;
    border-radius: 40px;
    overflow: hidden;
    box-shadow: 0 14px 30px rgba(0,0,0,.45);
  }
  .card--front { background: var(--card-white); border-bottom: 4px solid var(--brand-blue); }
  .card--back { background: linear-gradient(160deg, #262627 0%, var(--card-black) 60%, #151516 100%); border-bottom: 4px solid var(--brand-blue); }

  .brand {
    position: absolute;
    display: flex; align-items: center; gap: 22px;
  }
  .brand__dot {
    width: 34px; height: 34px; border-radius: 50%;
    background: var(--brand-blue);
    flex: none;
  }
  .brand__name {
    font-family: "Barlow", sans-serif;
    font-weight: 600;
    letter-spacing: 3px;
    text-transform: uppercase;
    line-height: 1;
  }
  .card--front .brand { left: 170px; top: 110px; }
  .card--front .brand__name { color: var(--ink-dark); font-size: 40px; }
  .card--back .brand { left: 50%; top: 50%; transform: translate(-50%, -50%); }
  .card--back .brand__dot { width: 46px; height: 46px; }
  .card--back .brand__name { color: var(--ink-light); font-size: 50px; }

  .person { position: absolute; left: 78px; bottom: 90px; }
  .person__name {
    font-family: "Montserrat", sans-serif; font-weight: 500;
    font-size: 42px; color: var(--brand-blue); text-transform: uppercase;
    line-height: 1;
  }
  .person__title {
    font-family: "Montserrat", sans-serif; font-weight: 400;
    font-size: 24px; color: var(--ink-dark); text-transform: uppercase;
    margin-top: 6px;
  }
  .divider {
    position: absolute; left: 500px; top: 255px;
    width: 1.5px; height: 130px; background: var(--rule-grey);
  }
  .contacts {
    position: absolute; left: 540px; top: 240px;
    list-style: none;
    font-family: "Montserrat", sans-serif; font-size: 19px; color: var(--ink-dark);
  }
  .contacts li { display: flex; align-items: flex-start; gap: 12px; line-height: 1.35; margin-bottom: 6px; }
  .contacts svg { width: 20px; height: 20px; flex: none; margin-top: 3px; fill: var(--brand-blue); }
</style>
</head>
<body>
<main class="canvas">
  <section class="card card--front" aria-label="Card front">
    <div class="brand">
      <span class="brand__dot"></span>
      <span class="brand__name">Quillbrook Sensing Systems</span>
    </div>

    <div class="person">
      <p class="person__name">Full Name</p>
      <p class="person__title">Title</p>
    </div>

    <span class="divider"></span>

    <ul class="contacts">
      <li>
        <svg viewBox="0 0 24 24" aria-hidden="true"><path d="M6.6 10.8a15 15 0 0 0 6.6 6.6l2.2-2.2c.3-.3.7-.4 1-.2 1.1.4 2.3.6 3.6.6.6 0 1 .4 1 1V20c0 .6-.4 1-1 1A17 17 0 0 1 3 4c0-.6.4-1 1-1h3.5c.6 0 1 .4 1 1 0 1.3.2 2.5.6 3.6.1.3 0 .7-.2 1z"/></svg>
        <span>(000) 000 0000</span>
      </li>
      <li>
        <svg viewBox="0 0 24 24" aria-hidden="true"><path d="M2 5h20v14H2zm2 2v.5l8 5 8-5V7zm0 3v7h16v-7l-8 5z"/></svg>
        <span>email@company.com</span>
      </li>
      <li>
        <svg viewBox="0 0 24 24" aria-hidden="true"><path d="M12 2a10 10 0 1 0 0 20 10 10 0 0 0 0-20zm6.9 6h-3a15 15 0 0 0-1.3-3.9A8 8 0 0 1 18.9 8zM12 4c.8 1.2 1.5 2.5 1.9 4h-3.8c.4-1.5 1.1-2.8 1.9-4zM4.3 14a8 8 0 0 1 0-4h3.4a16 16 0 0 0 0 4zm.8 2h3a15 15 0 0 0 1.3 3.9A8 8 0 0 1 5.1 16zm3-8h-3a8 8 0 0 1 4.3-3.9A15 15 0 0 0 8.1 8zM12 20c-.8-1.2-1.5-2.5-1.9-4h3.8c-.4 1.5-1.1 2.8-1.9 4zm2.3-6H9.7a14 14 0 0 1 0-4h4.6a14 14 0 0 1 0 4zm.3 5.9a15 15 0 0 0 1.3-3.9h3a8 8 0 0 1-4.3 3.9zm1.7-5.9a16 16 0 0 0 0-4h3.4a8 8 0 0 1 0 4z"/></svg>
        <span>www.company.com</span>
      </li>
      <li>
        <svg viewBox="0 0 24 24" aria-hidden="true"><path d="M12 2a7 7 0 0 0-7 7c0 5.2 7 13 7 13s7-7.8 7-13a7 7 0 0 0-7-7zm0 9.5a2.5 2.5 0 1 1 0-5 2.5 2.5 0 0 1 0 5z"/></svg>
        <span>123 Name Street, 000<br>Your City, 00000-000</span>
      </li>
    </ul>
  </section>

  <section class="card card--back" aria-label="Card back">
    <div class="brand">
      <span class="brand__dot"></span>
      <span class="brand__name">Quillbrook Sensing Systems</span>
    </div>
  </section>
</main>
</body>
</html>
```